Property Developer - Simple yet Sophisticated and Sharp Business Card

We are a medium sized property developer involved mainly in townhouse developments and land subdivisions.

The company is looking for a simple, sharp and sophisticated business card that will be given to contractors, land owners, financiers etc and thus will need to look professional.

Property development related graphics and art can be used, however the card is not to be too "busy" or crowded. Our company name is KL Estates which could possibly be incorporated into the graphics or artwork.

Single sided and/or double sided designs will be acceptable.

A Simple, Sophisticated, Sharp design please!

Good Luck !

```html
<!DOCTYPE html>
<html lang="en">
<head>
<meta charset="utf-8">
<title>KL Estates – Business Card</title>
<link href="https://fonts.googleapis.com/css2?family=Source+Sans+3:wght@400;600;700&display=swap" rel="stylesheet">
<style>
  :root{
    --stage:#000000;
    --card-top:#565656;
    --card-bottom:#3e3e3e;
    --sheen:rgba(120,120,120,.55);
    --sheen-clear:rgba(120,120,120,0);
    --text-main:#f2f2f2;
    --text-muted:#cfcfcf;
    --label:#a8a8a8;
  }
  html,body{margin:0;padding:0;overflow:hidden;}
  body{
    width:1200px;height:868px;background:var(--stage);
    font-family:"Source Sans 3", Arial, sans-serif;
    position:relative;
  }
  .card{
    position:absolute;top:292px;width:515px;height:285px;
    background:linear-gradient(160deg,var(--card-top),var(--card-bottom));
    overflow:hidden;
  }
  .card--front{left:50px;}
  .card--back{left:635px;}
  .card__artwork{position:absolute;inset:0;}
  .card--front .card__artwork{
    background:radial-gradient(ellipse 75% 65% at 85% 10%,var(--sheen),var(--sheen-clear) 70%);
  }
  .card--back .card__artwork{
    background:radial-gradient(ellipse 60% 80% at 10% 35%,var(--sheen),var(--sheen-clear) 70%);
  }
  .holder{position:absolute;left:41px;top:150px;text-align:center;}
  .holder__name{font-size:25px;color:var(--text-main);margin:0;line-height:1.1;font-weight:400;}
  .holder__role{font-size:20px;color:var(--text-muted);margin:2px 0 0;line-height:1.1;}
  .company-name{
    position:absolute;left:14px;top:248px;margin:0;
    font-size:30px;font-weight:700;letter-spacing:2px;text-transform:uppercase;
    color:var(--text-main);line-height:1;
  }
  .contact{
    position:absolute;left:240px;top:142px;margin:0;padding:0;list-style:none;
    font-size:16.5px;line-height:21px;color:var(--text-main);
  }
  .contact__label{color:var(--label);margin-right:3px;}
  .contact__indent{padding-left:17px;}
</style>
</head>
<body>

<section class="card card--front" aria-label="Front of business card">
  <div class="card__artwork" role="img" aria-label="Decorative curved swoosh pattern sweeping across the upper right"></div>
  <div class="holder">
    <p class="holder__name">Nadia Rahman</p>
    <p class="holder__role">President</p>
  </div>
  <p class="company-name">KL Estates</p>
</section>

<section class="card card--back" aria-label="Back of business card">
  <div class="card__artwork" role="img" aria-label="Decorative curved swoosh pattern arcing from the left edge"></div>
  <ul class="contact">
    <li><span class="contact__label">A:</span>PO Box 2714 Greenfield</li>
    <li class="contact__indent">North QLD 4217</li>
    <li><span class="contact__label">E:</span>info@klestates.com</li>
    <li><span class="contact__label">P:</span>(07) 5550 2146</li>
    <li><span class="contact__label">F:</span>(07) 5550 2147</li>
    <li><span class="contact__label">W:</span>www.klestates.com</li>
  </ul>
</section>

</body>
</html>
```